Events floral designer business needs a logo design

I need a logo design for my floral design business called tender thorns.
i am inspired by nature and the simplicity of its beauty, whilst upcycling and recycling materials to reduce waste and impact on our environment.
I would like the design to be printed on recycled brown cardboard so i would like a simple but striking design of a bold black ivy vine or gnarly magnolia or tree branch with lower case old school type writer font.

Target Market(s)

Anyone requiring floral additions for their event

Industry/Entity Type

Business

Contact Information for Business Card

mara hollis
floral designer/creator
0418657203
mara@tenderthorns.com
tenderthorns.com

Font styles to use
Other font styles liked:
• lower case type writer

Colors
000000

Requirements
Must have
• simplicity but boldness
• Black typewriter font and bold picture with my details
Nice to have
• as above
Should not have
• colour

```html
<!DOCTYPE html>
<html lang="en">
<head>
<meta charset="utf-8">
<title>tender thorns – business card</title>
<link rel="stylesheet" href="https://fonts.googleapis.com/css2?family=Courier+Prime:wght@400;700&display=swap">
<style>
  :root {
    --backdrop: #e9e6e1;
    --kraft: #c8a57c;
    --kraft-edge: #b8946a;
    --paper: #ffffff;
    --ink: #000000;
    --ink-soft: #222222;
    --shadow: rgba(60, 45, 30, 0.18);
  }
  * { box-sizing: border-box; margin: 0; padding: 0; }
  html, body {
    width: 1200px; height: 801px; overflow: hidden;
    background: var(--backdrop);
  }
  .sheet {
    width: 1200px; height: 801px;
    display: flex; align-items: center; justify-content: center; gap: 56px;
  }
  .card {
    width: 540px; height: 309px; position: relative; flex: none;
    box-shadow: 0 10px 28px var(--shadow);
  }
  .card--front { background: var(--kraft); border: 1px solid var(--kraft-edge); }
  .card--back { background: var(--paper); }

  .brand {
    position: absolute; display: flex; flex-direction: column; align-items: center; gap: 18px;
  }
  .brand__dot {
    width: 96px; height: 96px; border-radius: 50%; background: var(--ink);
  }
  .brand__name {
    font-family: "Courier Prime", "Courier New", monospace; font-size: 19px; letter-spacing: 0.34em;
    color: var(--ink); text-transform: lowercase; white-space: nowrap;
  }
  .card--front .brand { left: 0; right: 0; top: 72px; }
  .card--back .brand { left: 24px; width: 232px; top: 78px; }
  .card--back .brand__dot { width: 82px; height: 82px; }
  .card--back .brand__name { font-size: 15px; letter-spacing: 0.3em; }

  .contact { position: absolute; left: 282px; top: 100px; right: 24px; }
  .contact__name {
    font-family: "Courier Prime", "Courier New", monospace; font-weight: 700;
    font-size: 21px; letter-spacing: 0.28em; line-height: 1.2;
    color: var(--ink); text-transform: capitalize; white-space: nowrap;
  }
  .contact__role {
    font-family: "Courier Prime", "Courier New", monospace; font-size: 14px;
    letter-spacing: 0.02em; color: var(--ink-soft); margin-top: 4px;
  }
  .contact__list { list-style: none; margin-top: 20px; }
  .contact__item {
    display: flex; align-items: center; gap: 10px; margin-bottom: 6px;
    font-family: "Courier Prime", "Courier New", monospace; font-size: 14px;
    letter-spacing: 0.02em; color: var(--ink); white-space: nowrap;
  }
  .contact__icon { width: 13px; height: 13px; flex: none; }
</style>
</head>
<body>
<main class="sheet">
  <section class="card card--front" aria-label="Card front">
    <div class="brand">
      <span class="brand__dot"></span>
      <span class="brand__name">tender thorns</span>
    </div>
  </section>

  <section class="card card--back" aria-label="Card back">
    <div class="brand">
      <span class="brand__dot"></span>
      <span class="brand__name">tender thorns</span>
    </div>
    <div class="contact">
      <h1 class="contact__name">Mara Hollis</h1>
      <p class="contact__role">Floral designer/creator</p>
      <ul class="contact__list">
        <li class="contact__item">
          <svg class="contact__icon" viewBox="0 0 16 16" aria-hidden="true"><path fill="var(--ink)" d="M1 5c0-2 3-3 7-3s7 1 7 3v2h-3V5.5H4V7H1z M3 8h10l1 6H2z"/></svg>
          0418657203
        </li>
        <li class="contact__item">
          <svg class="contact__icon" viewBox="0 0 16 16" aria-hidden="true"><rect x="1" y="3" width="14" height="10" fill="var(--ink)"/><path d="M1 3l7 6 7-6" fill="none" stroke="#fff" stroke-width="1.2"/></svg>
          mara@tenderthorns.com
        </li>
        <li class="contact__item">
          <svg class="contact__icon" viewBox="0 0 16 16" aria-hidden="true"><g fill="none" stroke="var(--ink)" stroke-width="1.3"><circle cx="8" cy="8" r="6.5"/><ellipse cx="8" cy="8" rx="3" ry="6.5"/><path d="M1.5 8h13"/></g></svg>
          tenderthorns.com
        </li>
      </ul>
    </div>
  </section>
</main>
</body>
</html>
```